The name of the company is Kestrel Rehab buying foreclosed homes and remodeling

A sleek classy card. It’s a home remodel and house flip company. Something mostly black with dark gray and red in color . Something with two f”s as a logo on front as shown in pictures. Kind of just let you guys run with it . I left a few pictures that should help
You guys get an idea of what I thought was good also left all the information for back of the card

Target Market(s)

Home remodel consumers

Industry/Entity Type

Construction Company

Contact Information for Business Card

All details are on photo

Font styles to use
Decorative

Colors

Designer to choose colors to be used in the design.

Requirements
Must have
• Name of company on front. Kestrel Rehab
Nice to have
• Up to you guys I trust you
Should not have
• Not sure

```html
<!DOCTYPE html>
<html lang="en">
<head>
<meta charset="utf-8">
<title>Kestrel Rehab – Business Card</title>
<link href="https://fonts.googleapis.com/css2?family=Montserrat:wght@400;500;600&display=swap" rel="stylesheet">
<style>
  :root {
    --backdrop: #2e2927;
    --card: #151515;
    --ink: #dcdcdc;
    --ink-soft: #b9b9b9;
    --white: #ffffff;
  }
  * { box-sizing: border-box; margin: 0; padding: 0; }
  html, body { width: 1200px; height: 672px; overflow: hidden; }
  body {
    background: var(--backdrop);
    font-family: "Montserrat", sans-serif;
    color: var(--ink);
    position: relative;
  }
  .card {
    position: absolute;
    width: 310px;
    height: 540px;
    top: 66px;
    background: var(--card);
    overflow: hidden;
  }
  .card--back { left: 370px; }
  .card--front { left: 740px; }
  .card__face {
    position: absolute;
    width: 540px;
    height: 310px;
    left: -115px;
    top: 115px;
    transform: rotate(90deg);
  }
  .brand { display: flex; flex-direction: column; }
  .brand__row { display: flex; align-items: center; gap: 10px; }
  .brand__square { background: var(--ink); flex: none; }
  .brand__name {
    font-weight: 500;
    letter-spacing: 0.08em;
    color: var(--ink);
    line-height: 1;
    white-space: nowrap;
  }
  .brand__tagline {
    font-weight: 400;
    letter-spacing: 0.04em;
    color: var(--ink-soft);
    text-transform: uppercase;
    white-space: nowrap;
  }
  .card--back .brand { position: absolute; left: 48px; top: 52px; }
  .card--back .brand__square { width: 14px; height: 14px; }
  .card--back .brand__name { font-size: 24px; }
  .card--back .brand__tagline { font-size: 7px; margin-top: 6px; }
  .contact { position: absolute; left: 48px; top: 150px; }
  .contact__name {
    font-size: 19px;
    font-weight: 400;
    letter-spacing: 0.04em;
    margin-bottom: 14px;
  }
  .contact__list { list-style: none; }
  .contact__item {
    display: flex; align-items: center; gap: 8px;
    font-size: 11.5px; line-height: 20px; color: var(--ink);
  }
  .contact__icon { width: 10px; height: 10px; flex: none; }
  .card--front .brand {
    position: absolute; left: 0; right: 0; top: 96px;
    align-items: center;
  }
  .card--front .brand__square { width: 22px; height: 22px; }
  .card--front .brand__name { font-size: 36px; }
  .card--front .brand__tagline { font-size: 9px; margin-top: 8px; }
  .services {
    position: absolute; left: 0; right: 0; bottom: 34px;
    text-align: center; font-size: 12px; letter-spacing: 0.06em;
    color: var(--ink); text-transform: uppercase; white-space: nowrap;
  }
  .services__divider { margin: 0 8px; }
  .lockup { position: absolute; left: 28px; top: 480px; }
  .lockup .brand__square { width: 22px; height: 22px; background: var(--white); }
  .lockup .brand__name { font-size: 30px; color: var(--white); }
  .lockup .brand__tagline { font-size: 9.5px; margin-top: 8px; color: var(--ink); }
</style>
</head>
<body>

  <section class="card card--back">
    <div class="card__face">
      <div class="brand">
        <div class="brand__row">
          <span class="brand__square"></span>
          <span class="brand__name">KESTREL REHAB</span>
        </div>
        <span class="brand__tagline">Buying foreclosed homes and remodeling</span>
      </div>
      <div class="contact">
        <p class="contact__name">DANIEL HARCOURT JR.</p>
        <ul class="contact__list">
          <li class="contact__item">
            <svg class="contact__icon" viewBox="0 0 10 10"><path d="M2 1h2l1 2.5-1.3 1a5 5 0 0 0 2 2l1-1.3L9 6v2a1 1 0 0 1-1 1A7 7 0 0 1 1 2a1 1 0 0 1 1-1z" fill="#dcdcdc"/></svg>
            555 014 2276
          </li>
          <li class="contact__item">
            <svg class="contact__icon" viewBox="0 0 10 10"><rect x="0.5" y="2" width="9" height="6.5" fill="none" stroke="#dcdcdc"/><path d="M0.5 2l4.5 3.5L9.5 2" fill="none" stroke="#dcdcdc"/></svg>
            DHarcourtjr@mailbox.com
          </li>
          <li class="contact__item">
            <svg class="contact__icon" viewBox="0 0 10 10"><rect x="0.5" y="0.5" width="9" height="9" fill="#dcdcdc"/></svg>
            _Kestrel_Rehab_
          </li>
          <li class="contact__item">
            <svg class="contact__icon" viewBox="0 0 10 10"><circle cx="5" cy="5" r="4.5" fill="#dcdcdc"/></svg>
            www.kestrelrehab.com
          </li>
        </ul>
      </div>
    </div>
  </section>

  <section class="card card--front">
    <div class="card__face">
      <div class="brand">
        <div class="brand__row">
          <span class="brand__square"></span>
          <span class="brand__name">KESTREL REHAB</span>
        </div>
        <span class="brand__tagline">Buying foreclosed homes and remodeling</span>
      </div>
      <p class="services">
        General Contractor<span class="services__divider">|</span>Home Remodel<span class="services__divider">|</span>Concrete Alternatives
      </p>
    </div>
  </section>

  <div class="brand lockup">
    <div class="brand__row">
      <span class="brand__square"></span>
      <span class="brand__name">KESTREL REHAB</span>
    </div>
    <span class="brand__tagline">Buying foreclosed homes and remodeling</span>
  </div>

</body>
</html>
```